mailer to distressed properties

Our business is a company that buys houses for cash that are in need of repairs. Need to create a post card to mail to homeowners to get them to call us to give them a price on their home for cash and purchase it. Would like a run down house on background and our company info so they could call us. Have a logo would like to incorporate in it. Want to get to the point across we can buy there home for cash on any condition and close quickly. We can also buy them if they have permit or violation issues. We also buy homes going into foreclosure so we can stop foreclosure. Company name is R & T Dwellings. P o box 829 Westmere my 11947. 631-482-9163. Email us at info@randtdwellings.example and our website Randtdwellings.example. Open to a lot of direct designs excited to see what you come up with. Anything else you can think we are open to see it. Email us with any other questions . Also can add fast closing and save no real estate commissions collected. We want it in color your choice. Also on font open to anything and size of font.

Target Market(s)

Run down and distressed properties

Industry/Entity Type

Construction Company

Font styles to use
Serif
Sans Serif

Requirements
Must have
• A background of a distressed home and our info how to call us
Nice to have
• Colorful and attractive
Should not have
• Nothing I can think of

```html
<!DOCTYPE html>
<html lang="en">
<head>
<meta charset="utf-8">
<title>R &amp; T Dwellings Postcard</title>
<link rel="stylesheet" href="https://fonts.googleapis.com/css2?family=Archivo+Black&family=Alfa+Slab+One&family=Open+Sans:wght@400;600;700&family=PT+Sans+Narrow:wght@400;700&display=swap">
<style>
  :root {
    --bg: #ece6dc;
    --red: #d7191f;
    --red-band: rgba(206, 22, 30, 0.88);
    --yellow: #ffe812;
    --ink: #1a1a1a;
    --white: #ffffff;
    --sky: #b9dcef;
    --brick: #9a4a36;
    --brick-dark: #5b3327;
  }
  * { box-sizing: border-box; margin: 0; padding: 0; }
  html, body { width: 1200px; height: 411px; overflow: hidden; background: var(--bg); }
  .stage { position: relative; width: 1200px; height: 411px; }

  /* Front side */
  .card-front {
    position: absolute; left: 33px; top: 30px; width: 545px; height: 353px; overflow: hidden;
    box-shadow: 0 2px 6px rgba(0,0,0,.25);
  }
  .house-photo {
    position: absolute; inset: 0;
    background: linear-gradient(135deg, var(--brick) 0%, #b25a40 35%, var(--brick-dark) 70%, #7a6a60 100%);
  }
  .headline { position: absolute; left: 0; right: 0; text-align: center; line-height: 1; }
  .headline-top {
    top: 14px; font-family: "Archivo Black", sans-serif; font-size: 30px; color: var(--yellow);
    -webkit-text-stroke: 1.2px var(--red); paint-order: stroke fill;
  }
  .headline-main {
    top: 48px; font-family: "Alfa Slab One", serif; font-size: 37px; letter-spacing: 1px; color: var(--red);
    -webkit-text-stroke: 1.5px var(--yellow); paint-order: stroke fill;
  }
  .brand-tile {
    position: absolute; left: 365px; top: 198px; width: 154px; height: 34px; background: var(--white);
    display: flex; align-items: center; justify-content: center;
    font-family: "Open Sans", sans-serif; font-weight: 700; font-size: 20px; color: var(--red); letter-spacing: -0.5px;
  }
  .contact-band {
    position: absolute; left: 0; right: 0; top: 250px; bottom: 0; background: var(--red-band);
    text-align: center; color: var(--white); font-family: "Open Sans", sans-serif; padding-top: 8px;
  }
  .contact-band .lead { font-size: 17px; font-weight: 600; line-height: 21px; }
  .contact-band .lead strong { font-weight: 700; }
  .contact-band .email { font-size: 14px; font-weight: 600; line-height: 20px; }
  .contact-band .site { font-size: 20px; font-weight: 700; color: var(--yellow); margin-top: 8px; }
  .phone-icon { display: inline-block; width: 17px; height: 17px; vertical-align: -2px; }

  /* Back side */
  .card-back {
    position: absolute; left: 619px; top: 30px; width: 547px; height: 353px; overflow: hidden;
    background: linear-gradient(90deg, var(--sky) 0%, #e3f1f9 35%, var(--white) 55%);
    font-family: "PT Sans Narrow", sans-serif; color: var(--ink);
    box-shadow: 0 2px 6px rgba(0,0,0,.25);
  }
  .accent { color: var(--red); }
  .message { position: absolute; left: 0; top: 24px; width: 273px; text-align: center; }
  .message h2 { font-size: 14px; font-weight: 700; line-height: 16px; }
  .message .help { font-size: 14px; font-weight: 700; line-height: 17px; color: var(--red); }
  .message .intro { font-size: 9.5px; line-height: 13px; margin-top: 2px; white-space: nowrap; }
  .message .intro b { color: var(--red); font-weight: 700; }
  .easy-band {
    position: absolute; left: 0; top: 99px; width: 273px; height: 22px; background: var(--red);
    color: var(--white); font-weight: 700; font-size: 15px; text-align: center; line-height: 22px;
  }
  .steps, .perks {
    position: absolute; left: 28px; width: 235px; font-size: 9.5px; font-weight: 700; line-height: 11px; list-style: none;
  }
  .steps { top: 124px; }
  .steps .indent { padding-left: 10px; display: block; }
  .perks { top: 175px; }
  .perks li::before { content: "• "; }
  .perks .wrap { padding-left: 6px; }
  .thanks { position: absolute; left: 28px; top: 234px; font-size: 9.5px; font-weight: 700; line-height: 11px; }
  .call-block { position: absolute; left: 0; width: 273px; top: 263px; text-align: center; font-size: 11px; font-weight: 700; line-height: 14px; }
  .call-block .first { margin-bottom: 2px; }
  .call-block .red { color: var(--red); }
  .sender { position: absolute; left: 360px; top: 24px; font-family: "Open Sans", sans-serif; }
  .sender .name { font-size: 13px; font-weight: 700; color: var(--red); }
  .sender .addr { font-size: 7px; line-height: 10px; margin-top: 4px; }
  .stamp-box { position: absolute; left: 468px; top: 2px; width: 50px; height: 51px; border: 1.5px dashed #888; }
</style>
</head>
<body>
<div class="stage">

  <section class="card-front">
    <div class="house-photo" role="img" aria-label="Photo of a rundown brick house with weathered timber frame and broken windows"></div>
    <div class="headline headline-top">We Buy Rundown Houses</div>
    <div class="headline headline-main">FAST CASH SALES!</div>
    <div class="brand-tile">R&amp;T Dwellings</div>
    <div class="contact-band">
      <p class="lead">If you or anyone you know owns blighted, abandoned or<br>foreclosed property, <strong>CALL
        <svg class="phone-icon" viewBox="0 0 20 20"><circle cx="10" cy="10" r="8.5" fill="none" stroke="#fff" stroke-width="1.6"/><path d="M7 5.5c-1 1-1 3 1 5.5s4.5 3 5.5 2l-1.3-1.6-1.4.6c-1-.5-2-1.6-2.5-2.6l.6-1.4z" fill="#fff"/></svg>
        (631) 482-9163</strong></p>
      <p class="email">or Email us at info@randtdwellings.example</p>
      <p class="site">Randtdwellings.example</p>
    </div>
  </section>

  <section class="card-back">
    <div class="message">
      <h2>Need to sell your rundown house <span class="accent">FAST?</span></h2>
      <p class="help">We can help . . .</p>
      <p class="intro"><b>R&amp;T Dwellings</b> is a company that look for rundown houses in your area to<br>purchase for CASH.&nbsp; Because of our low overhead, we can offer you<br><b>TOP DOLLAR</b> for your house and get you cash <b>QUICK</b></p>
    </div>
    <div class="easy-band">It's easy!</div>
    <ol class="steps">
      <li>1. Call us</li>
      <li>2. We make you a <span class="accent">CASH</span> offer and explain everything<span class="indent">SIMPLY for you</span></li>
      <li>3. You accept or reject the offer, <span class="accent">NO OBLIGATION</span></li>
    </ol>
    <ul class="perks">
      <li>No commission fees or fees of ANY kind</li>
      <li>We pay the closing costs</li>
      <li>No need to do ANY repairs or even clean up, we take<br><span class="wrap">care of everything.</span></li>
      <li>You will receive the cash we promise in writing.</li>
    </ul>
    <p class="thanks">We have helped thousands of people. Help us to help you!</p>
    <div class="call-block">
      <p class="first">Call Us Today</p>
      <p class="red">(631) 482-9163</p>
      <p>or Email us at info@randtdwellings.example</p>
      <p class="red">Randtdwellings.example</p>
    </div>
    <div class="sender">
      <p class="name">R&amp;T Dwellings</p>
      <p class="addr">P.O. Box 829<br>Westmere NY 11947</p>
    </div>
    <div class="stamp-box"></div>
  </section>

</div>
</body>
</html>
```